Webdesign für Blog zum Thema KINDERWUNSCH
Zielgruppe
Hallo, ich bin 41 Jahre alt und lebe mit meinem Mann und unseren beiden Kindern (und Hund Ki;)) in einem kleinen Ort im Rhein-Main-Gebiet.
Ich musste auf meine beiden Kinder jeweils lange warten und diese schwere Zeit habe ich nicht vergessen. Meine beste Freundin hat mich irgendwann dazu überredet, anderen Frauen, denen es ähnlich geht, zu helfen. Besonders kann ich mich daran erinnern, wie schwer es war, verlässliche, gut recherchierte Quellen zum Thema Kinderwunsch zu finden.
Zusammen mit meiner besten Freundin baue ich daher einen Blog auf, bei dem es genau um diese Themen gehen soll.
Zielgruppe:
• Frauen
• Mitte / Ende 30
• Verheiratet, keine Kinder
• Höheres Bildungsniveau / nicht zwingend Akademiker
Kernemotionen:
o grübelt / ist unsicher
o nimmt ungewollte Kinderlosigkeit persönlich
o ängstlich / teils verzweifelt
o ungeduldig
Aufgabenstellung
Es geht um das Design unseres Blogs.
Uns ist besonders wichtig, dass der Blog das Spannungsverhältnis Seriosität – Freude – Ruhe vermittelt.
Das Design soll folgendes transportieren:
• Seriös / glaubwürdig
• Hochwertig
• Sicherheit / Ruhe / Seelenfriede
• Hoffnung
• Positiv / herzlich / unbeschwert – aber dennoch ernsthaft
ZUM FARBKONZEPT ETC. SIEHE BITTE BRIEFING ANBEI

```html
<!DOCTYPE html>
<html lang="de">
<head>
<meta charset="utf-8">
<title>Mein Wunschnest – Blogartikel</title>
<link href="https://fonts.googleapis.com/css2?family=Asap:wght@600;700&family=Ubuntu:wght@300;400;500&display=swap" rel="stylesheet">
<style>
:root{
  --teal:#4fb3bf;
  --teal-dark:#3e9ea9;
  --stripe:#e4f3f5;
  --ink:#333a3c;
  --muted:#8a9294;
  --white:#ffffff;
  --avatar:#2e3a3b;
}
*{box-sizing:border-box;margin:0;padding:0}
html,body{width:794px;height:1200px;overflow:hidden}
body{position:relative;background:var(--white);font-family:"Ubuntu",sans-serif;color:var(--ink)}
.site-header{position:absolute;left:0;top:0;width:794px;height:83px;background:var(--white)}
.menu-toggle{position:absolute;left:34px;top:36px;width:14px;height:12px}
.main-nav{position:absolute;left:68px;top:39px;display:flex;gap:16px;font-size:8px}
.main-nav a{color:var(--muted);text-decoration:none}
.main-nav a.active{color:var(--teal);font-weight:500}
.nav-badge{display:block;font-size:5px;color:var(--teal);margin-top:1px}
.brand{position:absolute;left:310px;top:20px;display:flex;align-items:center;gap:7px;color:var(--teal);font-weight:300}
.brand-dot{width:26px;height:26px;border-radius:50%;background:var(--teal)}
.brand-name{font-size:21px;line-height:1}
.search-icon{position:absolute;left:644px;top:34px}
.login-btn{position:absolute;left:671px;top:28px;width:91px;height:28px;background:var(--teal);border:2px solid var(--white);outline:1px solid var(--teal);color:var(--white);font-size:7px;font-weight:500;display:flex;align-items:center;justify-content:space-between;padding:0 12px 0 15px}
.stripes{position:absolute;left:0;top:83px;width:794px;height:1117px;background:repeating-linear-gradient(90deg,var(--stripe) 0 6px,var(--white) 6px 15.4px)}
.article{position:absolute;left:149px;top:101px;width:496px;height:676px;background:var(--white);box-shadow:0 1px 4px rgba(0,0,0,.06)}
.hero{width:496px;height:219px;background:linear-gradient(100deg,#8a8276 0%,#c9a48e 30%,#e07a5c 60%,#d9c3b0 100%)}
.article-title{font-family:"Asap",sans-serif;font-weight:700;color:var(--teal);font-size:18.5px;line-height:25px;text-align:center;margin-top:16px}
.article-lead{text-align:center;font-size:9px;font-weight:500;margin-top:10px}
.quote{position:relative;margin:33px 0 0 62px;width:372px;font-size:9.3px;line-height:12.2px}
.quote-mark{position:absolute;font-family:"Asap",sans-serif;font-weight:700;font-style:italic;color:var(--teal);font-size:22px;line-height:1}
.quote-mark.open{left:388px;top:-22px}
.quote-mark.close{left:-28px;top:46px}
.article-body{margin:35px 34px 0 34px;font-size:8px;line-height:12.1px;text-align:justify}
.article-body p+p{margin-top:12px}
.comments-title{position:absolute;left:184px;top:798px;font-size:11.5px;font-weight:400}
.comment{position:absolute;left:182px;width:400px}
.avatar{position:absolute;left:0;top:0;width:23px;height:23px;border-radius:50%;background:var(--avatar);border:2px solid #d8dcdc;color:var(--white);font-size:7px;font-weight:500;display:flex;align-items:center;justify-content:center}
.author{position:absolute;left:0;top:28px;font-size:6px;width:23px;text-align:center;white-space:nowrap}
.comment-box{position:absolute;left:36px;top:0;width:362px;background:var(--white);padding:10px 20px 10px 17px;box-shadow:0 2px 3px rgba(0,0,0,.05)}
.comment-date{position:absolute;right:6px;top:7px;font-size:6px;color:var(--muted)}
.comment-text{font-size:7.8px;line-height:11.6px;text-align:justify;width:296px}
.reply{display:block;font-size:6.3px;color:var(--teal);margin-top:12px}
.site-footer{position:absolute;left:0;top:1096px;width:794px;text-align:center;font-size:6.3px}
.footer-links{margin-top:4px;font-size:7px;font-weight:500;color:var(--teal)}
.social{display:flex;justify-content:center;gap:14px;margin-top:12px;font-size:6.5px;color:var(--teal);font-weight:500}
.social span{display:flex;align-items:center;gap:3px}
.social i{width:10px;height:10px;background:var(--teal);display:block}
</style>
</head>
<body>
<header class="site-header">
  <svg class="menu-toggle" viewBox="0 0 14 12"><g stroke="#4fb3bf" stroke-width="1.2"><line x1="0" y1="1" x2="14" y2="1"/><line x1="0" y1="6" x2="14" y2="6"/><line x1="0" y1="11" x2="14" y2="11"/></g></svg>
  <nav class="main-nav">
    <a class="active" href="#">Übersicht</a>
    <a href="#">Über mich</a>
    <a href="#">Forum<span class="nav-badge">● 2 neue Beiträge</span></a>
  </nav>
  <div class="brand"><span class="brand-dot"></span><span class="brand-name">Mein Wunschnest</span></div>
  <svg class="search-icon" width="14" height="14" viewBox="0 0 14 14"><circle cx="5.5" cy="5.5" r="4.3" fill="none" stroke="#4fb3bf" stroke-width="1.4"/><line x1="8.7" y1="8.7" x2="13" y2="13" stroke="#4fb3bf" stroke-width="2"/></svg>
  <a class="login-btn">Anmelden
    <svg width="11" height="11" viewBox="0 0 11 11"><circle cx="5.5" cy="5.5" r="5.5" fill="#fff"/><path d="M3 5.5h4.5M5.5 3.3l2.2 2.2-2.2 2.2" stroke="#4fb3bf" stroke-width="1.3" fill="none"/></svg>
  </a>
</header>

<div class="stripes"></div>

<article class="article">
  <div class="hero" role="img" aria-label="Foto: drei Freundinnen lachen gemeinsam an einem Cafétisch"></div>
  <h1 class="article-title">Freunde sind das Fundament für deinen<br>Wunsch nach Kindern</h1>
  <p class="article-lead">Ich erzähle Dir, wie mir eine Freundin helfen konnte.</p>
  <blockquote class="quote">
    <span class="quote-mark open">“</span>
    Lorem ipsum dolor sit amet, consetetur sadipscing elitr, sed diam nonumy eirmod tempor invidunt ut labore et dolore magna aliquyam erat, sed diam voluptua. At vero eos et accusam et justo duo dolores et ea rebum. Stet clita kasd gubergren, no sea takimata sanctus est Lorem ipsum dolor sit amet.
    <span class="quote-mark close">”</span>
  </blockquote>
  <div class="article-body">
    <p>Lorem ipsum dolor sit amet, consetetur sadipscing elitr, sed diam nonumy eirmod tempor invidunt ut labore et dolore magna aliquyam erat, sed diam voluptua. At vero eos et accusam et justo duo dolores et ea rebum. Stet clita kasd gubergren, no sea takimata sanctus est Lorem ipsum dolor sit amet. Lorem ipsum dolor sit amet, consetetur sadipscing elitr, sed diam nonumy eirmod tempor invidunt ut labore et dolore magna aliquyam erat, sed diam voluptua. At vero eos et accusam et justo duo dolores et ea rebum. Stet clita kasd gubergren, no sea takimata sanctus est Lorem ipsum dolor sit amet. Lorem ipsum dolor sit amet, consetetur sadipscing elitr, sed diam nonumy eirmod tempor invidunt ut labore et dolore magna aliquyam erat, sed diam voluptua. At vero eos et accusam et justo duo dolores et ea rebum. Stet clita kasd gubergren, no sea takimata sanctus est Lorem ipsum dolor sit amet.</p>
    <p>Duis autem vel eum iriure dolor in hendrerit in vulputate velit esse molestie consequat, vel illum dolore eu feugiat nulla facilisis at vero eros et accumsan et iusto odio dignissim qui blandit praesent luptatum zzril delenit augue duis dolore te feugait nulla facilisi. Lorem ipsum dolor sit amet, consectetuer adipiscing elit, sed diam nonummy nibh euismod tincidunt ut laoreet dolore magna aliquam erat volutpat.</p>
    <p>Ut wisi enim ad minim veniam, quis nostrud exerci tation ullamcorper suscipit lobortis nisl ut aliquip ex ea commodo consequat. Duis autem vel eum iriure dolor in hendrerit in vulputate velit esse molestie consequat, vel illum dolore eu feugiat nulla facilisis at vero eros et accumsan et iusto odio dignissim qui blandit praesent luptatum zzril delenit augue duis dolore te feugait nulla facilisi.</p>
  </div>
</article>

<h2 class="comments-title">2 Kommentare</h2>

<div class="comment" style="top:830px">
  <div class="avatar">MK</div><div class="author">Mia K.</div>
  <div class="comment-box" style="height:56px">
    <span class="comment-date">vor 2 Tagen</span>
    <p class="comment-text" style="margin-top:5px">Great job!</p>
    <span class="reply" style="margin-top:9px">Antworten</span>
  </div>
</div>

<div class="comment" style="top:913px">
  <div class="avatar">MK</div><div class="author">Mia K.</div>
  <div class="comment-box" style="height:146px">
    <span class="comment-date">vor 2 Tagen</span>
    <p class="comment-text" style="margin-top:4px">Lorem ipsum dolor sit amet, consetetur sadipscing elitr, sed diam nonumy eirmod tempor invidunt ut labore et dolore magna aliquyam erat, sed diam voluptua. At vero eos et accusam et justo duo dolores et ea rebum. Stet clita kasd gubergren, no sea takimata sanctus est Lorem ipsum dolor sit amet. Lorem ipsum dolor sit amet, consetetur sadipscing elitr, sed diam nonumy eirmod tempor invidunt ut labore et dolore magna aliquyam erat, sed diam voluptua. At vero eos et accusam et justo duo dolores et ea rebum. Stet clita kasd gubergren, no sea takimata sanctus est Lorem ipsum dolor sit amet.</p>
    <span class="reply">Antworten</span>
  </div>
</div>

<footer class="site-footer">
  <p>Copyright © 2017 Lena Hofmann</p>
  <p class="footer-links">Impressum | Kontakt</p>
  <div class="social"><span><i></i>Fotoblick</span><span><i></i>Freundeskreis</span></div>
</footer>
</body>
</html>
```